organic wine estate needs name and design for a new productline of fresh/low/no alcohol wines

we are a organic wine estate from austria and we need a name and labeldesign for a new productline of fresh/low/no alcoholwines. design should work for all 3 (fresh and low and no alcohol wines). potential customers are mainly between 20 and 40 years old. the label will be printed on structured natural-white paper, wrapped around the bottle (no front & back lable). the name should reflect the light and fresh winestyle. bottleshape will be burgundy-style, preferred colour dark green, with screwcap closure (colour matching the label).

```html
<!DOCTYPE html>
<html lang="en">
<head>
<meta charset="UTF-8">
<title>Hellrebe – No Alcohol Wines Label</title>
<link href="https://fonts.googleapis.com/css2?family=Cinzel:wght@600;700&family=Montserrat:wght@400;500&display=swap" rel="stylesheet">
<style>
  :root {
    --backdrop: #f4f4f4;
    --paper: #f1f1f0;
    --ink: #3b3b3b;
    --ink-soft: #555555;
    --emblem-light: #d9d9d9;
    --emblem-dark: #9a9a9a;
  }
  * { margin: 0; padding: 0; box-sizing: border-box; }
  html, body {
    width: 900px;
    height: 1200px;
    overflow: hidden;
    background: var(--backdrop);
  }
  .canvas {
    position: relative;
    width: 900px;
    height: 1200px;
  }
  .label {
    position: absolute;
    left: 30px;
    top: 264px;
    width: 840px;
    height: 672px;
    background: var(--paper);
    color: var(--ink);
    text-align: center;
  }
  .emblem {
    position: absolute;
    left: 50%;
    top: 80px;
    width: 143px;
    height: 143px;
    transform: translateX(-50%);
  }
  .brand-name {
    position: absolute;
    left: 0;
    right: 0;
    top: 300px;
    font-family: "Cinzel", serif;
    font-weight: 700;
    font-size: 104px;
    line-height: 1;
    letter-spacing: 1px;
    color: var(--ink);
  }
  .product-line {
    position: absolute;
    left: 0;
    right: 0;
    top: 428px;
    font-family: "Montserrat", sans-serif;
    font-weight: 400;
    font-size: 30px;
    letter-spacing: 1.5px;
    color: var(--ink);
  }
  .details {
    position: absolute;
    left: 0;
    right: 0;
    top: 604px;
    display: flex;
    justify-content: center;
    align-items: center;
    font-family: "Montserrat", sans-serif;
    color: var(--ink-soft);
  }
  .details .claim {
    text-align: right;
    font-size: 18px;
    line-height: 1.15;
    padding-right: 10px;
    border-right: 2px solid var(--ink-soft);
  }
  .details .volume {
    font-size: 23px;
    padding-left: 10px;
  }
</style>
</head>
<body>
  <main class="canvas">
    <section class="label">
      <svg class="emblem" viewBox="0 0 143 143" role="img" aria-label="Round engraved seal with a bunch of grapes and vine leaves">
        <defs>
          <radialGradient id="emblem-fill" cx="50%" cy="50%" r="50%">
            <stop offset="0%" stop-color="var(--emblem-dark)"/>
            <stop offset="100%" stop-color="var(--emblem-light)"/>
          </radialGradient>
        </defs>
        <circle cx="71.5" cy="71.5" r="70" fill="url(#emblem-fill)"/>
      </svg>

      <h1 class="brand-name">Hellrebe</h1>
      <p class="product-line">NO ALCOHOL WINES</p>

      <div class="details">
        <p class="claim">Zero Alcohol<br>100% Vibes</p>
        <p class="volume">750 ml.</p>
      </div>
    </section>
  </main>
</body>
</html>
```